Online medical reviews website needs banner advert!

We need banner advert templates for our website, www.traineepanel.net. These should meet the technical requirements of our partner (uploaded).

Our groundbreaking website allows doctors in training to rate and review their training.

The adverts should use the same modern design language and colour scheme as our website. They should use the text 'Help a junior doctor make a big decision - rate your training!'.

Vector assets should be supplied, allowing us to use alternative text in future.
Updates

Industry/Entity Type

Healthcare

Font styles to use
Other font styles liked:
• Karla

Colors
3277b5
0555a3
ffffff

Requirements
Must have
• Similar design to our website. Should be elegant & modern. Must allow future text to be easily inserted.
Should not have
• Unrelated design.

```html
<!DOCTYPE html>
<html lang="en">
<head>
<meta charset="utf-8">
<title>Trainee Panel – Banner Set</title>
<link rel="stylesheet" href="https://fonts.googleapis.com/css2?family=Arimo:wght@400;700&display=swap">
<style>
  :root {
    --navy: #0b2d8e;
    --navy-light: #2a4ea8;
    --white: #ffffff;
    --stage-top: #bfbfbf;
    --stage-mid: #ececec;
    --stage-bottom: #bdbdbd;
    --slash: rgba(255,255,255,0.55);
  }
  * { box-sizing: border-box; margin: 0; padding: 0; }
  html, body { width: 1200px; height: 1200px; overflow: hidden; }
  body {
    position: relative;
    font-family: "Arimo", Arial, sans-serif;
    background: radial-gradient(ellipse at 50% 50%, var(--stage-mid) 0%, var(--stage-top) 100%);
  }
  .banner { position: absolute; overflow: hidden; background: var(--navy); color: var(--white); }
  .banner svg { position: absolute; inset: 0; width: 100%; height: 100%; display: block; }
  .banner .copy { position: absolute; }
  .subline { font-weight: 400; letter-spacing: -0.5px; line-height: 1.05; white-space: nowrap; }
  .headline { font-weight: 700; letter-spacing: -1px; line-height: 1; white-space: nowrap; }
  .brand {
    position: absolute; display: flex; align-items: center; gap: 8px;
    font-weight: 400; color: var(--white); letter-spacing: -0.5px; white-space: nowrap;
  }
  .brand .mark { display: inline-block; background: var(--white); }

  /* Skyscraper */
  .banner--tall { left: 94px; top: 44px; width: 472px; height: 940px; }
  .banner--tall .copy { left: 0; right: 0; text-align: center; }
  .banner--tall .subline { top: 490px; font-size: 35px; }
  .banner--tall .headline { top: 608px; font-size: 78px; line-height: 0.98; }
  .banner--tall .brand { left: 0; right: 0; top: 836px; justify-content: center; font-size: 42px; }
  .banner--tall .brand .mark { width: 16px; height: 16px; }

  /* Medium rectangles */
  .banner--rect-a { left: 599px; top: 44px; width: 515px; height: 428px; }
  .banner--rect-b { left: 606px; top: 552px; width: 508px; height: 424px; }
  .banner--rect-a .copy, .banner--rect-b .copy { left: 24px; }
  .banner--rect-a .subline, .banner--rect-b .subline { font-size: 22px; }
  .banner--rect-a .headline, .banner--rect-b .headline { font-size: 46px; }
  .banner--rect-a .subline { top: 332px; }
  .banner--rect-a .headline { top: 362px; }
  .banner--rect-a .brand { left: 24px; top: 322px; font-size: 30px; }
  .banner--rect-a .brand { top: 278px; }
  .banner--rect-b .brand { left: 24px; top: 275px; font-size: 30px; }
  .banner--rect-b .subline { top: 328px; }
  .banner--rect-b .headline { top: 358px; }
  .banner--rect-a .brand .mark, .banner--rect-b .brand .mark { width: 11px; height: 11px; }

  /* Leaderboard */
  .banner--wide { left: 90px; top: 1016px; width: 1039px; height: 128px; }
  .banner--wide .copy { left: 22px; }
  .banner--wide .subline { top: 24px; font-size: 29px; }
  .banner--wide .headline { top: 60px; font-size: 41px; }
  .banner--wide .brand { left: 432px; top: 74px; font-size: 20px; gap: 6px; }
  .banner--wide .brand .mark { width: 8px; height: 8px; }
</style>
</head>
<body>

<section class="banner banner--tall" aria-label="Skyscraper banner">
  <svg viewBox="0 0 472 940" preserveAspectRatio="none">
    <defs>
      <linearGradient id="tallPhoto" x1="0" y1="0" x2="1" y2="1">
        <stop offset="0" stop-color="#e4ddd6"/>
        <stop offset="0.45" stop-color="#cfae8f"/>
        <stop offset="1" stop-color="#3a4f86"/>
      </linearGradient>
    </defs>
    <rect x="0" y="0" width="472" height="470" fill="url(#tallPhoto)" role="img" aria-label="Photo: patient simulation manikin beside a monitoring screen"/>
    <polygon points="0,446 472,332 472,360 0,452" fill="var(--slash)"/>
    <polygon points="0,450 472,360 472,940 0,940" fill="var(--navy)"/>
  </svg>
  <p class="copy subline">Help a junior doctor<br>make a big decision...</p>
  <h2 class="copy headline">Rate your<br>training!</h2>
  <div class="brand"><span>Trainee Panel</span><span class="mark"></span></div>
</section>

<section class="banner banner--rect-a" aria-label="Medium rectangle banner, simulation">
  <svg viewBox="0 0 515 428" preserveAspectRatio="none">
    <defs>
      <linearGradient id="rectPhotoA" x1="0" y1="0" x2="1" y2="1">
        <stop offset="0" stop-color="#3b5bd6"/>
        <stop offset="0.5" stop-color="#6f7a88"/>
        <stop offset="1" stop-color="#e2c7a8"/>
      </linearGradient>
    </defs>
    <rect x="0" y="0" width="515" height="290" fill="url(#rectPhotoA)" role="img" aria-label="Photo: gloved hands performing intubation practice on a training manikin"/>
    <polygon points="0,210 515,278 515,428 0,428" fill="var(--navy)"/>
    <polygon points="300,250 515,278 515,316" fill="var(--navy-light)"/>
  </svg>
  <div class="brand"><span>Trainee Panel</span><span class="mark"></span></div>
  <p class="copy subline">Help a junior doctor make a big decision...</p>
  <h2 class="copy headline">Rate your training!</h2>
</section>

<section class="banner banner--rect-b" aria-label="Medium rectangle banner, team">
  <svg viewBox="0 0 508 424" preserveAspectRatio="none">
    <defs>
      <linearGradient id="rectPhotoB" x1="0" y1="0" x2="1" y2="0">
        <stop offset="0" stop-color="#e9eef0"/>
        <stop offset="0.45" stop-color="#5f8fc9"/>
        <stop offset="1" stop-color="#b08a5e"/>
      </linearGradient>
    </defs>
    <rect x="0" y="0" width="508" height="310" fill="url(#rectPhotoB)" role="img" aria-label="Photo: group of junior doctors in scrubs walking down a hospital corridor"/>
    <polygon points="0,168 508,300 508,310 0,208" fill="var(--slash)"/>
    <polygon points="0,208 508,308 508,424 0,424" fill="var(--navy)"/>
  </svg>
  <div class="brand"><span>Trainee Panel</span><span class="mark"></span></div>
  <p class="copy subline">Help a junior doctor make a big decision...</p>
  <h2 class="copy headline">Rate your training!</h2>
</section>

<section class="banner banner--wide" aria-label="Leaderboard banner">
  <svg viewBox="0 0 1039 128" preserveAspectRatio="none">
    <defs>
      <linearGradient id="widePhoto" x1="0" y1="0" x2="1" y2="1">
        <stop offset="0" stop-color="#0f3c4a"/>
        <stop offset="0.5" stop-color="#3c7f8c"/>
        <stop offset="1" stop-color="#0b2a38"/>
      </linearGradient>
    </defs>
    <polygon points="710,0 1039,0 1039,128 606,128" fill="url(#widePhoto)" role="img" aria-label="Photo: surgical team in masks and caps at an operating table"/>
    <polygon points="700,0 718,0 614,128 596,128" fill="var(--slash)"/>
  </svg>
  <p class="copy subline">Help a junior doctor make a big decision...</p>
  <h2 class="copy headline">Rate your training!</h2>
  <div class="brand"><span>Trainee Panel</span><span class="mark"></span></div>
</section>

</body>
</html>
```